Brimvantel

We are re-branding the company with a new logo (attached) which I would
like to go on one side of the card, and I have attached a file showing what
the old back side looked like, and I do like the characters that show the
phone, e-mails, etc., I don't like the current arrangement, and I want
something clean, clear and out of the box, as we are an aviation consulting
firm, and we work outside of the box.

```html
<!DOCTYPE html>
<html lang="en">
<head>
<meta charset="utf-8">
<title>Brimvantel – Business Card</title>
<link rel="stylesheet" href="https://fonts.googleapis.com/css2?family=Open+Sans:wght@400;600;700&display=swap">
<style>
  :root {
    --backdrop: #e6e6e6;
    --card: #ffffff;
    --brand-red: #8c1014;
    --ink: #2b2b2b;
    --muted: #6f6f6f;
    --ribbon-red: #e8202a;
    --ribbon-blue: #1ba3dc;
    --ribbon-green: #7dc242;
    --ribbon-orange: #f7a21b;
    --icon-pin: #e8202a;
    --icon-globe: #1ba3dc;
    --icon-phone: #7dc242;
  }
  * { box-sizing: border-box; margin: 0; padding: 0; }
  html, body {
    width: 1200px; height: 1200px; overflow: hidden;
    background: var(--backdrop);
    font-family: "Open Sans", Arial, sans-serif;
    color: var(--ink);
  }
  .sheet {
    width: 1200px; height: 1200px;
    display: flex; flex-direction: column;
    align-items: center; justify-content: center; gap: 56px;
  }
  .card {
    position: relative;
    width: 900px; height: 514px;
    background: var(--card);
    overflow: hidden;
    box-shadow: 0 6px 22px rgba(0,0,0,.12);
  }

  /* Back side */
  .services {
    position: absolute; left: 0; top: 92px;
    display: flex; flex-direction: column; gap: 6px;
  }
  .service {
    height: 34px;
    padding-left: 42px;
    color: #fff; font-size: 17px; font-weight: 400; letter-spacing: .4px;
    line-height: 34px;
    clip-path: polygon(0 0, 100% 0, calc(100% - 22px) 100%, 0 100%);
  }
  .service--finance { width: 380px; background: var(--ribbon-red); }
  .service--technical { width: 365px; background: var(--ribbon-blue); }
  .service--consulting { width: 350px; background: var(--ribbon-green); }
  .service--restructuring { width: 335px; background: var(--ribbon-orange); }

  .contact {
    position: absolute; right: 56px; top: 66px;
    text-align: right;
  }
  .contact__name { font-size: 25px; font-weight: 400; letter-spacing: 1px; }
  .contact__title { font-size: 17px; margin-top: 2px; letter-spacing: .5px; }
  .contact__list { list-style: none; margin-top: 26px; display: flex; flex-direction: column; gap: 18px; }
  .contact__item {
    display: flex; align-items: center; justify-content: flex-end; gap: 14px;
    font-size: 15px; line-height: 1.35; letter-spacing: .4px;
  }
  .contact__icon { width: 22px; height: 22px; flex: none; }

  .signoff {
    position: absolute; right: 56px; bottom: 44px;
    display: flex; align-items: center; gap: 10px;
  }
  .signoff__dot { width: 14px; height: 14px; border-radius: 50%; background: var(--brand-red); }
  .signoff__name { font-size: 24px; font-weight: 600; color: var(--brand-red); letter-spacing: 1px; }

  /* Front side */
  .front__field {
    position: absolute; inset: 0;
    background: var(--brand-red);
    clip-path: polygon(36% 100%, 100% 20%, 100% 100%);
  }
  .brand {
    position: absolute; left: 150px; top: 150px;
    display: flex; flex-direction: column; align-items: flex-start;
  }
  .brand__row { display: flex; align-items: center; gap: 18px; }
  .brand__dot { width: 38px; height: 38px; border-radius: 50%; background: var(--brand-red); }
  .brand__name { font-size: 64px; font-weight: 600; color: var(--brand-red); letter-spacing: 3px; line-height: 1; }
  .brand__tagline { margin-top: 10px; margin-left: 58px; font-size: 19px; color: var(--muted); letter-spacing: 1.2px; }
</style>
</head>
<body>
<main class="sheet">

  <section class="card card--back" aria-label="Card back">
    <div class="services">
      <div class="service service--finance">Aircraft finance/leasing</div>
      <div class="service service--technical">Technical services</div>
      <div class="service service--consulting">Aviation consulting</div>
      <div class="service service--restructuring">Airline restructuring</div>
    </div>

    <div class="contact">
      <p class="contact__name">Dorian K. Halvers</p>
      <p class="contact__title">President &amp; CEO</p>
      <ul class="contact__list">
        <li class="contact__item">
          <span>2740B Willow Run<br>Fairhaven, CA 90417</span>
          <svg class="contact__icon" viewBox="0 0 24 24" aria-hidden="true">
            <path d="M12 2a7 7 0 0 0-7 7c0 5 7 13 7 13s7-8 7-13a7 7 0 0 0-7-7z" fill="var(--icon-pin)"/>
            <circle cx="12" cy="9" r="2.6" fill="#fff"/>
          </svg>
        </li>
        <li class="contact__item">
          <span>Web-www.brv.aero</span>
          <svg class="contact__icon" viewBox="0 0 24 24" aria-hidden="true">
            <circle cx="12" cy="12" r="10" fill="var(--icon-globe)"/>
            <g fill="none" stroke="#fff" stroke-width="1.3">
              <ellipse cx="12" cy="12" rx="4.5" ry="10"/>
              <line x1="2" y1="12" x2="22" y2="12"/>
              <path d="M4 7h16M4 17h16"/>
            </g>
          </svg>
        </li>
        <li class="contact__item">
          <span>+1 555 014 2286<br>+1 555 017 3390</span>
          <svg class="contact__icon" viewBox="0 0 24 24" aria-hidden="true">
            <rect x="3" y="3" width="18" height="18" rx="2" fill="none" stroke="var(--icon-phone)" stroke-width="2.4"/>
          </svg>
        </li>
      </ul>
    </div>

    <div class="signoff">
      <span class="signoff__dot"></span>
      <span class="signoff__name">Brimvantel</span>
    </div>
  </section>

  <section class="card card--front" aria-label="Card front">
    <div class="front__field"></div>
    <div class="brand">
      <div class="brand__row">
        <span class="brand__dot"></span>
        <span class="brand__name">Brimvantel</span>
      </div>
      <p class="brand__tagline">trusted experience • proven solutions</p>
    </div>
  </section>

</main>
</body>
</html>
```